Website offering services oriented to the metaverse and blockchain

We need an ecommerce website theme/template for a new company named Vamplo (a play on words for MERIDAK the inventor of Zenthal). Vamplo will provide metaverse services such as:
• Vamplo Coin
• Vamplo wallet
• Vamplo Exchange
• Vamplo NFT
• Vamplo Tech
• Vamplo Pay
• Vamplo CaaS (community as a service)
• Vamplo CRM
• Vamplo Experience
• Vamplo Blockchain
• Vamplo Commerce
• Vamplo Space (as in outer space)
• Vamplo Art (sub of NFT)
• Vamplo Store

You can find our actual logo at the following link, in order to show us templates aligned with our brand:
https://files.vamplo-share.example/folders/7kWpLmQzRtYb3NxVcHsJd92AeFgUoPiKw?view=open

Looking forward to heard back from you,

Designs look the same

We need a WordPress ecommerce website theme/template for a new company named Vamplo (a play on words for MERIDAK the inventor of Zenthal). Vamplo will provide metaverse services such as: • Vamplo Coin • Vamplo wallet • Vamplo Exchange • Vamplo NFT • Vamplo Tech • Vamplo Pay • Vamplo CaaS (community as a service) • Vamplo CRM • Vamplo Experience • Vamplo Blockchain • Vamplo Commerce • Vamplo Space (as in outer space) • Vamplo Art (sub of NFT) • Vamplo Store You can find our actual logo at the following link, in order to show us templates aligned with our brand: https://files.vamplo-share.example/folders/7kWpLmQzRtYb3NxVcHsJd92AeFgUoPiKw?view=open Looking forward to heard back from you,

Target Market(s)

Blockchain & Cryptocurrency Businesses

Industry/Entity Type

B2C, B2B Services.

Font styles to use
Other font styles liked:
• Monserrat, Helvetica, Object Sans

Requirements
Nice to have
• Light background picture,
Should not have
• Arch designs

```html
<!DOCTYPE html>
<html lang="en">
<head>
<meta charset="utf-8">
<title>Vamplo</title>
<link href="https://fonts.googleapis.com/css2?family=Roboto:wght@400;500;700;900&display=swap" rel="stylesheet">
<style>
:root{
  --ink:#0f0c45;
  --hero:#0f1820;
  --blue:#2392f0;
  --orange:#fa9208;
  --purple:#8a10ee;
  --purple-deep:#6d0bd0;
  --white:#ffffff;
  --dark:#111111;
}
*{margin:0;padding:0;box-sizing:border-box}
html,body{width:1200px;height:4409px;overflow:hidden}
body{font-family:"Roboto",Helvetica,Arial,sans-serif;color:var(--white);background:var(--ink);position:relative}
section,header,footer{position:absolute;left:0;width:1200px;overflow:hidden}
.abs{position:absolute}
.bar{position:absolute;height:4px;width:80px;background:var(--orange)}
.btn{position:absolute;display:flex;align-items:center;justify-content:center;border-radius:5px;font-weight:700}
.btn-orange{background:var(--orange);color:var(--dark)}
h2{font-weight:700;color:var(--blue)}
p{font-size:13px;line-height:30px}

/* hero */
.hero{top:0;height:608px;background:var(--hero)}
.brand{left:112px;top:38px;font-size:29px;font-weight:700}
.nav a{position:absolute;top:54px;font-size:13px;color:var(--white);text-decoration:none}
.login{left:847px;top:36px;width:113px;height:48px;background:var(--purple);font-size:13px;font-weight:500}
.register{left:976px;top:36px;width:112px;height:48px;border:2px solid var(--white);font-size:13px;font-weight:500}
.hero-art{left:560px;top:120px;width:640px;height:488px;background:radial-gradient(ellipse at 55% 45%,#1d8fe8 0%,#0d3f7a 35%,#0f1820 75%)}
.hero-kicker{left:112px;top:168px;font-size:49px;font-weight:700;color:var(--blue)}
.hero-title{left:112px;top:244px;font-size:58px;line-height:73px;font-weight:700;width:560px}
.hero .btn-orange{left:112px;top:484px;width:239px;height:64px;font-size:17px}

/* about */
.about{top:608px;height:642px;background:var(--ink)}
.about-photo{left:111px;top:122px;width:450px;height:420px;border-radius:8px;background:linear-gradient(135deg,#3a4450,#c9ced4 60%,#6d747c)}
.about h2{position:absolute;left:600px;top:140px;font-size:46px}
.about .bar{left:600px;top:210px}
.about p{position:absolute;left:600px;top:240px;width:495px}
.about .btn-orange{left:600px;top:456px;width:187px;height:54px;font-size:14px}

/* services */
.services{top:1250px;height:912px;background:linear-gradient(180deg,var(--purple) 0%,#7d0ee8 50%,var(--purple-deep) 100%)}
.center{left:0;width:1200px;text-align:center}
.eyebrow{top:56px;font-size:16px;font-weight:500}
.services h2.sec{top:84px;color:var(--white)}
.sec{position:absolute;left:0;width:1200px;text-align:center;font-size:42px}
.services .bar{left:560px;top:148px;background:var(--white)}
.lead{top:170px;font-size:15px}
.card{position:absolute;width:302px;height:287px;background:var(--ink);border-radius:6px;text-align:center}
.card.active{background:var(--orange)}
.card svg{position:absolute;left:116px;top:44px}
.card h3{position:absolute;left:0;width:100%;top:134px;font-size:15px;font-weight:700}
.card p{position:absolute;left:22px;width:258px;top:162px;font-size:12.5px;line-height:26px}

/* why */
.why{top:2162px;height:685px;background:var(--ink)}
.why h2{position:absolute;left:69px;top:128px;font-size:46px}
.why .bar{left:69px;top:208px}
.why p.intro{position:absolute;left:69px;top:236px;width:490px}
.feature{position:absolute;width:300px}
.feature svg{position:absolute;left:0;top:0}
.feature h4{position:absolute;left:81px;top:0;color:var(--orange);font-size:15px;font-weight:500;white-space:nowrap}
.feature p{position:absolute;left:81px;top:22px;width:210px;font-size:13px;line-height:26px}
.laptop{left:692px;top:278px;width:508px;height:340px;border-radius:14px 0 0 6px;background:linear-gradient(135deg,#0d3a66,#2e8fd4 45%,#9c2c6a 80%,#1a1a2a)}
.laptop-base{left:614px;top:618px;width:586px;height:22px;border-radius:0 0 0 18px;background:linear-gradient(180deg,#8a8d94,#3a3c42)}

/* certifications */
.certs{top:2847px;height:573px;background:linear-gradient(180deg,#1a0a52,#2a0c6a 55%,#150a4a)}
.certs h2.sec{top:64px}
.certs .bar{left:560px;top:128px}
.cert{position:absolute;top:183px;width:310px;height:308px;background:var(--purple);border-radius:4px}
.cert-img{position:absolute;left:24px;top:24px;width:262px;height:204px;background:linear-gradient(160deg,#f4f4f6,#d8dbe4)}
.cert-img.dark{background:linear-gradient(135deg,#1c1c1c 55%,#e4b818)}
.cert span{position:absolute;left:0;width:100%;top:252px;text-align:center;font-size:21px;font-weight:700}
.arrow{position:absolute;top:307px}

/* team */
.team{top:3420px;height:555px;background:var(--ink)}
.team h2.sec{top:56px}
.team .bar{left:560px;top:133px}
.member{position:absolute;top:185px;width:222px;text-align:center}
.avatar{width:222px;height:222px;border-radius:50%;border:4px solid var(--white);background:linear-gradient(160deg,#d9d2c4,#8a7a66)}
.member h5{margin-top:30px;font-size:15px;font-weight:700}
.member small{display:block;margin-top:8px;font-size:13px}

/* footer */
.footer{top:3975px;height:434px;background:var(--orange);color:var(--dark)}
.col{position:absolute;top:62px}
.col h6{font-size:16px;font-weight:500;letter-spacing:.3px}
.col .rule{width:32px;height:2px;background:var(--dark);margin:12px 0 16px}
.col li{list-style:none;font-size:13.5px;line-height:30px}
.col b{display:block;font-size:13px;font-weight:700;margin-top:4px}
.col .txt{font-size:13.5px;line-height:22px}
.email{position:absolute;left:809px;top:182px;width:277px;height:40px;border-radius:20px;background:var(--ink);color:var(--white);font-size:12px;padding:13px 20px}
.email svg{position:absolute;right:14px;top:10px}
.social{position:absolute;top:266px;width:50px;height:50px;border:2px solid var(--dark);border-radius:50%}
.rule-full{position:absolute;left:110px;top:364px;width:980px;height:1px;background:var(--dark)}
.copy{position:absolute;top:392px;font-size:13.5px}
</style>
</head>
<body>

<header class="hero">
  <div class="abs brand">Vamplo</div>
  <nav class="nav">
    <a style="left:422px" href="#">Home</a>
    <a style="left:489px" href="#">About Us</a>
    <a style="left:575px" href="#">Service</a>
    <a style="left:650px" href="#">Certifications</a>
    <a style="left:763px" href="#">Contact Us</a>
  </nav>
  <div class="btn login">Login</div>
  <div class="btn register">Register</div>
  <div class="abs hero-art" role="img" aria-label="Glowing blue coin on a digital platform"></div>
  <div class="abs hero-kicker">Vamplo</div>
  <h1 class="abs hero-title">Cryptocurrency Makes Everything Better.</h1>
  <div class="btn btn-orange">GET STARTED</div>
</header>

<section class="about">
  <div class="abs about-photo" role="img" aria-label="Hands holding a tablet showing trading charts"></div>
  <h2>About Us</h2>
  <div class="bar"></div>
  <p>Lorem ipsum dolor sit amet, consectetur adipiscing elit, sed do eiusmod tempor incididunt ut labore et dolore magna aliqua. Ut enim ad minim veniam, quis nostrud exercitation ullamco laboris nisi ut aliquip ex ea commodo consequat. Duis aute irure dolor in reprehenderit in voluptate velit esse cillum dolore eu fugiat nulla pariatur. Excepteur sint occaecat cupidatat non proident, sunt in culpa qui officia deserunt mollit anim id est laborum</p>
  <div class="btn btn-orange">READ MORE</div>
</section>

<section class="services">
  <div class="abs center eyebrow">OUR SERVICE</div>
  <h2 class="sec">What We offer</h2>
  <div class="bar"></div>
  <div class="abs center lead">Lorem ipsum dolor sit amet, consectetur adipiscing elit, sed do eiusmod tempor</div>

  <div class="card" style="left:128px;top:236px">
    <svg width="70" height="70" viewBox="0 0 70 70" fill="none" stroke="#fa9208" stroke-width="3"><circle cx="35" cy="35" r="31"/><circle cx="35" cy="35" r="22"/></svg>
    <h3>Cryptocurrencies</h3>
    <p>Lorem ipsum dolor sit amet, adipiscing elit, sed do eiusmod tempor incididunt ut labore et dolore magna aliqua.</p>
  </div>
  <div class="card active" style="left:449px;top:236px">
    <svg width="70" height="70" viewBox="0 0 70 70" fill="none" stroke="#111" stroke-width="3"><circle cx="35" cy="35" r="31"/><circle cx="35" cy="35" r="22"/></svg>
    <h3>Precious metals</h3>
    <p>Lorem ipsum dolor sit amet, adipiscing elit, sed do eiusmod tempor incididunt ut labore et dolore magna aliqua.</p>
  </div>
  <div class="card" style="left:770px;top:236px">
    <svg width="70" height="70" viewBox="0 0 70 70" fill="none" stroke="#fa9208" stroke-width="3"><rect x="6" y="46" width="9" height="18"/><rect x="22" y="38" width="9" height="26"/><rect x="38" y="44" width="9" height="20"/><rect x="54" y="28" width="9" height="36"/><polyline points="10,32 26,18 42,26 60,8"/><circle cx="10" cy="32" r="3"/><circle cx="26" cy="18" r="3"/><circle cx="42" cy="26" r="3"/><circle cx="60" cy="8" r="3"/></svg>
    <h3>Stocks</h3>
    <p>Lorem ipsum dolor sit amet, adipiscing elit, sed do eiusmod tempor incididunt ut labore et dolore magna aliqua.</p>
  </div>
  <div class="card" style="left:128px;top:536px">
    <svg width="70" height="70" viewBox="0 0 70 70" fill="none" stroke="#fa9208" stroke-width="3"><circle cx="24" cy="38" r="16"/><circle cx="46" cy="34" r="16"/><path d="M30 8 a26 26 0 0 1 30 12"/><path d="M40 64 a26 26 0 0 1 -30 -12"/></svg>
    <h3>Environmental Assets</h3>
    <p>Lorem ipsum dolor sit amet, adipiscing elit, sed do eiusmod tempor incididunt ut labore et dolore magna aliqua.</p>
  </div>
  <div class="card" style="left:449px;top:536px">
    <svg width="70" height="70" viewBox="0 0 70 70" fill="none" stroke="#fa9208" stroke-width="3"><rect x="14" y="12" width="52" height="34" rx="3"/><rect x="4" y="24" width="52" height="34" rx="3"/><line x1="4" y1="34" x2="56" y2="34"/><rect x="10" y="44" width="14" height="8"/></svg>
    <h3>Debit Card</h3>
    <p>Lorem ipsum dolor sit amet, adipiscing elit, sed do eiusmod tempor incididunt ut labore et dolore magna aliqua.</p>
  </div>
  <div class="card" style="left:770px;top:536px">
    <svg width="70" height="70" viewBox="0 0 70 70" fill="none" stroke="#fa9208" stroke-width="3"><circle cx="35" cy="35" r="13"/><path d="M38 29 h-5 a3 3 0 0 0 0 6 h4 a3 3 0 0 1 0 6 h-5 M35 26 v18"/><path d="M14 22 l8 -10 l6 6"/><path d="M56 48 l-8 10 l-6 -6"/><path d="M48 10 l10 4 l-2 8"/><path d="M22 60 l-10 -4 l2 -8"/></svg>
    <h3>Automated trading</h3>
    <p>Lorem ipsum dolor sit amet, adipiscing elit, sed do eiusmod tempor incididunt ut labore et dolore magna aliqua.</p>
  </div>
</section>

<section class="why">
  <h2>Why Choose Vamplo</h2>
  <div class="bar"></div>
  <p class="intro">Lorem ipsum dolor sit amet, consectetur adipiscing elit, sed do eiusmod tempor incididunt ut labore et dolore magna aliqua. Ut enim ad minim veniam, quis nostrud exercitation ullamco laboris nisi ut</p>

  <div class="feature" style="left:69px;top:376px">
    <svg width="66" height="60" viewBox="0 0 66 60" fill="none" stroke="#fa9208" stroke-width="2.5"><path d="M33 4 l12 6 v12 l-12 6 l-12 -6 v-12z"/><path d="M14 32 l12 6 v12 l-12 6 l-12 -6 v-12z"/><path d="M52 32 l12 6 v12 l-12 6 l-12 -6 v-12z"/></svg>
    <h4>Multichain with device</h4>
    <p>Lorem ipsum dolor sit consectetur adipiscing elit, sed do</p>
  </div>
  <div class="feature" style="left:385px;top:376px">
    <svg width="66" height="60" viewBox="0 0 66 60" fill="none" stroke="#fa9208" stroke-width="2.5"><circle cx="40" cy="16" r="13"/><path d="M2 44 h14 l10 -6 h16 a4 4 0 0 1 0 8 h-12 M16 56 h24 l20 -14 a4 4 0 0 0 -6 -6 l-12 8"/></svg>
    <h4>Initial coin offering</h4>
    <p>Lorem ipsum dolor sit consectetur adipiscing elit, sed do</p>
  </div>
  <div class="feature" style="left:69px;top:494px">
    <svg width="66" height="60" viewBox="0 0 66 60" fill="none" stroke="#fa9208" stroke-width="2.5"><ellipse cx="36" cy="38" rx="24" ry="17"/><circle cx="34" cy="14" r="11"/><path d="M12 32 l-8 -2 v10 l8 2 M24 52 v6 M46 52 v6"/></svg>
    <h4>Payment integration</h4>
    <p>Lorem ipsum dolor sit consectetur adipiscing elit, sed do</p>
  </div>
  <div class="feature" style="left:385px;top:494px">
    <svg width="66" height="60" viewBox="0 0 66 60" fill="none" stroke="#fa9208" stroke-width="2.5"><rect x="4" y="14" width="58" height="40" rx="3"/><path d="M24 14 v-8 h18 v8 M4 32 h58"/><rect x="28" y="28" width="10" height="8"/></svg>
    <h4>Full data ownership</h4>
    <p>Lorem ipsum dolor sit consectetur adipiscing elit, sed do</p>
  </div>

  <div class="abs laptop" role="img" aria-label="Laptop screen showing a trader at work with market charts"></div>
  <div class="abs laptop-base"></div>
</section>

<section class="certs">
  <h2 class="sec">Cryptocurrency Certifications</h2>
  <div class="bar"></div>
  <svg class="arrow" style="left:57px" width="34" height="34" viewBox="0 0 34 34" fill="none" stroke="#fff" stroke-width="1.5"><circle cx="17" cy="17" r="15.5"/><polyline points="19,11 13,17 19,23"/></svg>
  <svg class="arrow" style="left:1107px" width="34" height="34" viewBox="0 0 34 34" fill="none" stroke="#fff" stroke-width="1.5"><circle cx="17" cy="17" r="15.5"/><polyline points="15,11 21,17 15,23"/></svg>
  <div class="cert" style="left:111px"><div class="cert-img" role="img" aria-label="Certificate of appreciation"></div><span>Lorem ipsum</span></div>
  <div class="cert" style="left:446px"><div class="cert-img" role="img" aria-label="Framed certificate with ornate border"></div><span>Lorem ipsum</span></div>
  <div class="cert" style="left:780px"><div class="cert-img dark" role="img" aria-label="Black and gold award certificate"></div><span>Lorem ipsum</span></div>
</section>

<section class="team">
  <h2 class="sec">Team Members</h2>
  <div class="bar"></div>
  <div class="member" style="left:127px"><div class="avatar" role="img" aria-label="Team member portrait"></div><h5>Dana Whitlow</h5><small>Lorem ipsum</small></div>
  <div class="member" style="left:373px"><div class="avatar" role="img" aria-label="Team member portrait"></div><h5>Dana Whitlow</h5><small>Lorem ipsum</small></div>
  <div class="member" style="left:618px"><div class="avatar" role="img" aria-label="Team member portrait"></div><h5>Dana Whitlow</h5><small>Lorem ipsum</small></div>
  <div class="member" style="left:864px"><div class="avatar" role="img" aria-label="Team member portrait"></div><h5>Dana Whitlow</h5><small>Lorem ipsum</small></div>
</section>

<footer class="footer">
  <div class="col" style="left:110px">
    <h6>QUICK LINKS</h6><div class="rule"></div>
    <ul><li>Home</li><li>About Us</li><li>Service</li><li>Certificate</li><li>Contact Us</li></ul>
  </div>
  <div class="col" style="left:312px">
    <h6>SERVICES</h6><div class="rule"></div>
    <ul><li>Cryptocurrencies</li><li>Precious metals</li><li>Stocks</li><li>Environmental Assets</li><li>Debit Card</li></ul>
  </div>
  <div class="col" style="left:554px;width:220px">
    <h6>CONTACT US</h6><div class="rule"></div>
    <b>ADDRESS</b><div class="txt">Lorem ipsum dolor sit amet, consectetur adipiscing</div>
    <b style="margin-top:10px">PHONE</b><div class="txt">&#9990; 123-555-0198</div>
    <b style="margin-top:14px">EMAIL</b><div class="txt">info@vamplo.example</div>
  </div>
  <div class="col" style="left:812px;width:280px">
    <h6>NEWSLETTER</h6><div class="rule"></div>
    <div class="txt">Lorem ipsum dolor sit amet, consectetur adipiscing elit, sed do eiusmod tempor</div>
  </div>
  <div class="email">Enter Email
    <svg width="20" height="20" viewBox="0 0 20 20"><circle cx="10" cy="10" r="10" fill="#fa9208"/><path d="M5 10 l10 -4 l-4 10 l-1 -4z" fill="#0f0c45"/></svg>
  </div>
  <div class="social" style="left:815px" aria-label="Professional network"></div>
  <div class="social" style="left:872px" aria-label="Social network"></div>
  <div class="social" style="left:929px" aria-label="Photo network"></div>
  <div class="rule-full"></div>
  <div class="copy" style="left:110px">&copy; 2021 Vamplo All Rights Reserved</div>
  <div class="copy" style="left:903px;font-size:12.5px">Terms of use | Privacy Policy</div>
</footer>

</body>
</html>
```